Jewelry Shop Needs a Business Card Design

***We want a very sharp and unforgettable pantone for the Business Card. ***
***We do not want the business card or logo only in black, white and grey color!!!Please provide us a main color as our brand topic! Thanks!! ***

Mabel’s Nook is a Hong Kong based fine jewelry brand.

We want a very nice, simple and elegant business card design for Mabel's Nook Brand. The company's logo has been uploaded already.

You can design with below info:

Dorian Fung
Director
M: +852 94273658
T: +852 35820417
F: +852 35820419
E: dorian.fung@mabelsnook.example
5/F , Harbourlight Tower, 12-18 Orchid Lane, Wan Tung Kok, Kowloon, Hong Kong

Target Market(s)

Mabel’s Nook philosophy is a jewelry icon of young, creative, trendy, fashionable, stylish, energetic, and elegant. For Mabel’s Nook, jewelry is one collection of artworks, the most important items in personal life.

Industry/Entity Type

Jewelry

Requirements
Must have
• We want a very sharp and unforgettable pantone for the Business Card.

```html
<!DOCTYPE html>
<html lang="en">
<head>
<meta charset="utf-8">
<title>Mabel’s Nook — Business Card</title>
<link rel="stylesheet" href="https://fonts.googleapis.com/css2?family=Cinzel:wght@400;500&display=swap">
<style>
  :root {
    --backdrop: #e8e4de;
    --card-top: #3a3a3a;
    --card-mid: #1a1a1a;
    --card-deep: #0b0b0b;
    --ink-light: #f4f4f4;
    --ink-soft: #d6d6d6;
    --brand: #c8234f;
    --brand-soft: #e25578;
  }
  * { margin: 0; padding: 0; box-sizing: border-box; }
  html, body {
    width: 1200px;
    height: 913px;
    overflow: hidden;
    background: var(--backdrop);
    font-family: "Cinzel", "Times New Roman", serif;
  }
  .canvas {
    position: relative;
    width: 1200px;
    height: 913px;
  }
  .card {
    position: absolute;
    width: 560px;
    height: 320px;
    border-radius: 4px;
    background: linear-gradient(150deg, var(--card-top) 0%, var(--card-mid) 45%, var(--card-deep) 100%);
    box-shadow: 0 10px 26px rgba(0, 0, 0, 0.28);
    color: var(--ink-light);
    overflow: hidden;
  }
  .card::after {
    content: "";
    position: absolute;
    left: 0;
    right: 0;
    bottom: 0;
    height: 6px;
    background: var(--brand);
  }
  .card--front { left: 70px; top: 70px; }
  .card--back  { left: 570px; top: 520px; }

  .brand-dot {
    position: absolute;
    border-radius: 50%;
    background: var(--brand);
  }
  .card--front .brand-dot { width: 132px; height: 132px; left: 150px; top: 62px; }
  .card--back  .brand-dot { width: 96px;  height: 96px;  left: 70px;  top: 92px; }

  .brand-name {
    position: absolute;
    font-weight: 400;
    letter-spacing: 0.06em;
    white-space: nowrap;
    color: var(--ink-light);
  }
  .card--front .brand-name { left: 120px; top: 218px; font-size: 27px; }
  .card--back  .brand-name { left: 52px;  top: 204px; font-size: 17px; }

  .contact {
    position: absolute;
    left: 290px;
    top: 40px;
    font-size: 11px;
    line-height: 1.45;
    color: var(--ink-soft);
    letter-spacing: 0.03em;
    white-space: nowrap;
  }
  .contact__name {
    font-size: 16px;
    color: var(--ink-light);
    line-height: 1.1;
  }
  .contact__role {
    font-size: 10px;
    color: var(--brand-soft);
    margin-bottom: 16px;
  }
  .contact__lines { list-style: none; margin-bottom: 16px; }
  .contact__address { font-style: normal; }
</style>
</head>
<body>
  <main class="canvas">
    <section class="card card--front" aria-label="Business card front">
      <span class="brand-dot"></span>
      <h1 class="brand-name">Mabel’s Nook</h1>
    </section>

    <section class="card card--back" aria-label="Business card back">
      <span class="brand-dot"></span>
      <p class="brand-name">Mabel’s Nook</p>
      <div class="contact">
        <p class="contact__name">Dorian Fung</p>
        <p class="contact__role">Director</p>
        <ul class="contact__lines">
          <li>M: +852 94273658</li>
          <li>T: +852 35820417</li>
          <li>F: +852 35820419</li>
          <li>E: dorian.fung@mabelsnook.example</li>
        </ul>
        <address class="contact__address">
          5/F , Harbourlight Tower,<br>
          12-18 Orchid Lane, Wan Tung Kok,<br>
          Kowloon, Hong Kong
        </address>
      </div>
    </section>
  </main>
</body>
</html>
```